Onlineshop VORMA braucht ein Design!
Zielgruppe
Wir entwickeln innovative Produkte. Für dieses Projekt haben wir 2 Zielgruppen: Kinder und Erwachsene.
Hallo,
wir haben ein neuartiges Tragesystem entwickelt, das dem Träger der Tasche das Tragen erleichtert. Im Moment arbeiten wir daran, dieses System für eine eigene Schultaschenlinie zu verwenden. Später wollen wir unsere Produktpalette erweitern und ebenso Zubehör hierzu(z.B. Regenschirm, Mütze etc.) mit anbieten. Als weiterer Schritt sind zudem auch andere Taschen (z.B. Rucksäcke) für Erwachsene geplant.
Unser Produkt ist einmalig und genau deshalb möchten wir eine Homepage mit Shopware 4 Community Edition eine prägnanten und übersichtlichen Shop, sowie ein Blog erstellen.
Das Logo für unser Schultaschenprojekt befindet sich im Anhang und kann farblich angepasst werden. Wir benötigen einen kindergerechten, gleichzeitig seriösen Internetauftritt und es kann auch gerne ein komplettes Template erstellt werden für Shopware 4 oder ein Design-Vorschlag (Photoshop) eingebracht werden.
Wir bitten euch die Photoshop-Design Vorlagen ohne verbundene Ebenen und Pfade anzulegen. Bei Templates, bitten wir um eine genauere detaillierte Information zum Aufbau, Struktur etc..

```html
<!DOCTYPE html>
<html lang="de">
<head>
<meta charset="utf-8">
<title>VORMA – Onlineshop</title>
<link href="https://fonts.googleapis.com/css2?family=Ubuntu:wght@400;500;700&family=Arimo:wght@400;700&display=swap" rel="stylesheet">
<style>
:root{
  --orange:#f07020;
  --orange-light:#f69a3c;
  --orange-dark:#e2560f;
  --tab:#f58a1e;
  --panel:#eeeeec;
  --panel-border:#dcdcdc;
  --gray-band:#c4c4c4;
  --gray-light:#dedede;
  --text:#707070;
  --text-dark:#555;
  --white:#fff;
}
html,body{margin:0;padding:0;width:1029px;height:1200px;overflow:hidden;background:var(--white);}
.page{position:relative;width:1200px;height:1400px;transform:scale(0.8575);transform-origin:0 0;font-family:"Arimo",Arial,sans-serif;color:var(--text);}
.abs{position:absolute;}
.band{position:absolute;left:101px;width:1002px;height:46px;background:linear-gradient(90deg,var(--orange-dark) 0%,var(--orange) 40%,var(--orange-light) 60%,var(--orange-dark) 100%);}
.band::before{content:"";position:absolute;left:0;top:0;width:25px;height:100%;background:var(--tab);}
.band-label,.gray-label{position:absolute;left:40px;top:0;line-height:46px;font-family:"Ubuntu",sans-serif;font-weight:500;font-size:11.5px;color:var(--white);text-transform:uppercase;}
.band-label::before,.gray-label::before,.nav a::before,.contact-head span::before,.about h2::before,.forgot::before,.login-btn::before{content:"›";margin-right:5px;font-weight:700;}
.gray-bar{position:absolute;height:46px;background:linear-gradient(90deg,#bfbfbf 0%,#cfcfcf 30%,#e8e8e8 50%,#c4c4c4 75%,#bdbdbd 100%);}
.gray-bar::before{content:"";position:absolute;left:0;top:0;width:25px;height:100%;background:#d0d0d0;}
.gray-label{color:var(--text-dark);}
.header{left:101px;top:48px;width:1002px;height:209px;background:linear-gradient(90deg,#e6e6e6,#f4f4f4 50%,#ececec);}
.brand{left:120px;top:70px;font-family:"Ubuntu",sans-serif;font-weight:700;font-size:56px;color:#a8a8a8;letter-spacing:4px;}
.brand-dot{left:345px;top:82px;width:22px;height:22px;border-radius:50%;background:var(--orange);}
.about{left:428px;top:15px;width:510px;}
.about h2{margin:0 0 10px;font-family:"Ubuntu",sans-serif;font-weight:400;font-size:12px;color:var(--text);}
.about h2 b{color:var(--orange);}
.about p{margin:0;font-family:"Ubuntu",sans-serif;font-size:11.4px;line-height:17px;}
.about p em{font-style:normal;color:var(--orange);}
.field{top:131px;height:36px;border:1px solid #c8c8c8;background:#efefef;font-family:"Ubuntu",sans-serif;font-size:11px;color:#888;line-height:36px;padding-left:22px;box-sizing:border-box;}
.login-btn{left:900px;top:132px;width:88px;height:35px;background:var(--orange);color:var(--white);font-family:"Ubuntu",sans-serif;font-size:11.5px;line-height:35px;text-align:center;}
.forgot{left:700px;top:171px;font-size:11px;color:#777;}
.nav{position:absolute;left:40px;top:0;line-height:46px;margin:0;padding:0;list-style:none;display:flex;}
.nav a{font-family:"Ubuntu",sans-serif;font-weight:500;font-size:11.5px;color:var(--white);text-decoration:none;margin-right:36px;}
.slider{left:101px;top:355px;width:1002px;height:300px;background:#e7e7e5;border:1px solid var(--panel-border);box-sizing:border-box;}
.slider-photo{left:13px;top:10px;width:978px;height:278px;background:linear-gradient(90deg,#e8b8a0 0%,#f2d6c6 30%,#f7e4d8 55%,#f0c8b4 75%,#f4f0ee 100%);}
.slider-cap{left:13px;top:10px;width:978px;height:62px;background:rgba(70,70,70,.95);color:var(--white);}
.slider-cap h3{margin:8px 0 2px 24px;font-family:"Ubuntu",sans-serif;font-weight:400;font-size:15px;letter-spacing:1.5px;}
.slider-cap p{margin:0 0 0 26px;font-size:10.5px;line-height:13px;}
.slider-cap a{color:#f5a623;text-decoration:none;}
.news{position:absolute;width:499px;height:210px;background:var(--panel);border:1px solid #e2e2e2;box-sizing:border-box;}
.news .band{left:-1px;top:-1px;width:499px;}
.news-body{position:absolute;left:12px;top:56px;right:10px;font-size:10.5px;line-height:13px;}
.news-photo{float:left;width:152px;height:100px;margin:0 14px 4px 0;border:2px solid #d6d6d6;background:linear-gradient(90deg,#8a9a6e,#c46a4c 35%,#d49a5a 65%,#8b7a5a);}
.news-body p{margin:0 0 13px;}
.contact{left:843px;top:1102px;width:260px;height:190px;background:var(--panel);border:1px solid #e2e2e2;box-sizing:border-box;}
.contact-head{position:absolute;left:-1px;top:-1px;width:260px;height:46px;background:linear-gradient(90deg,var(--orange-dark),var(--orange),var(--orange-dark));}
.contact-head::before{content:"";position:absolute;left:0;top:0;width:25px;height:100%;background:var(--tab);}
.contact-head span{position:absolute;left:40px;line-height:46px;font-family:"Ubuntu",sans-serif;font-weight:500;font-size:11.5px;color:var(--white);}
.contact address{position:absolute;left:44px;top:60px;font-style:normal;font-size:12px;line-height:14.5px;color:#666;}
.footer{left:0;top:1343px;width:1206px;text-align:center;font-size:12px;color:#777;}
</style>
</head>
<body>
<div class="page">
  <div class="band" style="top:0"><span class="band-label">Herzlich Willkommen auf VORMA.DE</span></div>

  <div class="abs header">
    <div class="abs brand-dot"></div>
    <div class="abs brand">VORMA</div>
    <div class="abs about">
      <h2>ÜBER <b>VORMA</b></h2>
      <p>Lorem ipsum dolor sit amet, consetetur sadipscing elitr, sed diam <em>nonumy</em> eirmod tempor nvidunt ut labore et dolore magna aliquyam erat, sed diam voluptua. At vero eos et accusam et justo duo dolores et ea rebum. Stet <em>clita</em> kasd gubergren, no sea takimata sanctus est Lorem ipsum dolor sit amet. Lorem ipsum dolor sit amet, consetetur <em>sadipscing</em> elitr, sed diam nonu</p>
    </div>
    <svg class="abs" style="left:427px;top:134px" width="28" height="28" viewBox="0 0 28 28" aria-hidden="true"><circle cx="10" cy="8" r="5" fill="#c89a5a"/><path d="M2 26c0-7 4-10 8-10s8 3 8 10z" fill="#8a8a8a"/><circle cx="19" cy="11" r="4" fill="#d9a86a"/><path d="M13 26c0-6 3-9 6-9s7 3 7 9z" fill="#e58a2a"/></svg>
    <div class="abs field" style="left:466px;width:194px">KUNDENNUMMER</div>
    <svg class="abs" style="left:668px;top:131px" width="26" height="32" viewBox="0 0 26 32" aria-hidden="true"><circle cx="9" cy="7" r="5" fill="none" stroke="#888" stroke-width="3"/><path d="M9 12v18M9 22h5M9 27h4" stroke="#888" stroke-width="3"/><circle cx="18" cy="8" r="4" fill="none" stroke="#b0b0b0" stroke-width="2.5"/><path d="M18 12v16" stroke="#b0b0b0" stroke-width="2.5"/></svg>
    <div class="abs field" style="left:699px;width:194px">***********</div>
    <div class="abs login-btn">LOGIN</div>
    <div class="abs forgot">Passwort vergessen ?</div>
  </div>

  <nav class="band" style="top:258px">
    <ul class="nav">
      <li><a href="#">STARTSEITE</a></li>
      <li><a href="#">ÜBER VORMA</a></li>
      <li><a href="#">BLOG</a></li>
      <li><a href="#">UNSER SYSTEM</a></li>
      <li><a href="#">PRODUKTE</a></li>
      <li><a href="#">SHOP</a></li>
      <li><a href="#">COMMUNITY</a></li>
      <li><a href="#">AGB</a></li>
    </ul>
  </nav>

  <div class="gray-bar" style="left:101px;top:305px;width:1002px"><span class="gray-label">UNSERE NEUESTEN ANGEBOT FINDEN SIE IM SLIDER</span></div>

  <section class="abs slider">
    <div class="abs slider-photo" role="img" aria-label="Foto: vier lachende Kinder liegen nebeneinander, Kinn auf die Hände gestützt"></div>
    <div class="abs slider-cap">
      <h3>DAS NEUE SYSTEM</h3>
      <p>Lorem ipsum dolor sit amet, consetetur sadipscing elitr, sed diam nonumy eirmod tempor invidunt ut labore et dolore magna aliquyam erat, sed diam voluptua.<br>At vero eos et accusam et justo duo dolores et ea rebum. Stet clita kasd gubergren, no sea takimata sanctus est Lorem ipsum dolor sit amet. <a href="#">mehr lesen</a></p>
    </div>
  </section>

  <article class="news" style="left:101px;top:665px"><div class="band"><span class="band-label">Die News Box von VORMA.DE</span></div>
    <div class="news-body"><div class="news-photo" role="img" aria-label="Foto: zwei Kinder mit bunten Schulranzen von hinten"></div><p>Lorem ipsum dolor sit amet, consetetur sadipscing elitr, sed diam nonumy eirmod tempor invidunt ut labore et dolore magna aliquyam erat, sed diam voluptua. At vero eos et accusam et justo duo dolores et ea rebum. Stet clita kasd gubergren, no sea takimata sanctus est Lorem ipsum dolor sit amet.</p><p>Lorem ipsum dolor sit amet, consetetur sadipscing elitr, sed diam nonumy eirmod tempor invidunt ut labore et dolore magna aliquyam erat, sed diam voluptua. At vero eos et accusam et justo duo dolores et ea rebum. Stet clita kasd gubergren, no sea takimata sanctus est Lorem ipsum dolor sit amet.magna aliquyam erat, sed diam voluptua.</p></div>
  </article>
  <article class="news" style="left:604px;top:665px"><div class="band"><span class="band-label">Neuigkeiten über VORMA</span></div>
    <div class="news-body"><div class="news-photo" role="img" aria-label="Foto: zwei Kinder mit bunten Schulranzen von hinten"></div><p>Lorem ipsum dolor sit amet, consetetur sadipscing elitr, sed diam nonumy eirmod tempor invidunt ut labore et dolore magna aliquyam erat, sed diam voluptua. At vero eos et accusam et justo duo dolores et ea rebum. Stet clita kasd gubergren, no sea takimata sanctus est Lorem ipsum dolor sit amet.</p><p>Lorem ipsum dolor sit amet, consetetur sadipscing elitr, sed diam nonumy eirmod tempor invidunt ut labore et dolore magna aliquyam erat, sed diam voluptua. At vero eos et accusam et justo duo dolores et ea rebum. Stet clita kasd gubergren, no sea takimata sanctus est Lorem ipsum dolor sit amet.magna aliquyam erat, sed diam voluptua.</p></div>
  </article>
  <article class="news" style="left:101px;top:879px"><div class="band"><span class="band-label">Neuigkeiten über VORMA</span></div>
    <div class="news-body"><div class="news-photo" role="img" aria-label="Foto: zwei Kinder mit bunten Schulranzen von hinten"></div><p>Lorem ipsum dolor sit amet, consetetur sadipscing elitr, sed diam nonumy eirmod tempor invidunt ut labore et dolore magna aliquyam erat, sed diam voluptua. At vero eos et accusam et justo duo dolores et ea rebum. Stet clita kasd gubergren, no sea takimata sanctus est Lorem ipsum dolor sit amet.</p><p>Lorem ipsum dolor sit amet, consetetur sadipscing elitr, sed diam nonumy eirmod tempor invidunt ut labore et dolore magna aliquyam erat, sed diam voluptua. At vero eos et accusam et justo duo dolores et ea rebum. Stet clita kasd gubergren, no sea takimata sanctus est Lorem ipsum dolor sit amet.magna aliquyam erat, sed diam voluptua.</p></div>
  </article>
  <article class="news" style="left:604px;top:879px"><div class="band"><span class="band-label">Neuigkeiten über VORMA</span></div>
    <div class="news-body"><div class="news-photo" role="img" aria-label="Foto: zwei Kinder mit bunten Schulranzen von hinten"></div><p>Lorem ipsum dolor sit amet, consetetur sadipscing elitr, sed diam nonumy eirmod tempor invidunt ut labore et dolore magna aliquyam erat, sed diam voluptua. At vero eos et accusam et justo duo dolores et ea rebum. Stet clita kasd gubergren, no sea takimata sanctus est Lorem ipsum dolor sit amet.</p><p>Lorem ipsum dolor sit amet, consetetur sadipscing elitr, sed diam nonumy eirmod tempor invidunt ut labore et dolore magna aliquyam erat, sed diam voluptua. At vero eos et accusam et justo duo dolores et ea rebum. Stet clita kasd gubergren, no sea takimata sanctus est Lorem ipsum dolor sit amet.magna aliquyam erat, sed diam voluptua.</p></div>
  </article>

  <div class="gray-bar" style="left:101px;top:1102px;width:741px"><span class="gray-label">DIE NEUESTEN BLOG EINTRÄGE SEHEN SIE INDEM SIE HIER AUF DIESEM LINK KLICKEN</span></div>
  <div class="gray-bar" style="left:101px;top:1150px;width:741px"><span class="gray-label">DIE NEUESTEN BLOG EINTRÄGE SEHEN SIE INDEM SIE HIER AUF DIESEM LINK KLICKEN</span></div>
  <div class="gray-bar" style="left:101px;top:1198px;width:741px"><span class="gray-label">DIE NEUESTEN BLOG EINTRÄGE SEHEN SIE INDEM SIE HIER AUF DIESEM LINK KLICKEN</span></div>
  <div class="gray-bar" style="left:101px;top:1246px;width:741px"><span class="gray-label">DIE NEUESTEN BLOG EINTRÄGE SEHEN SIE INDEM SIE HIER AUF DIESEM LINK KLICKEN</span></div>

  <aside class="abs contact">
    <div class="contact-head"><span>KONTAKTMÖGLICHKEITEN</span></div>
    <address>Jonas Feldner<br>Feldner GmbH<br>Lindenweg 14<br>12345 Auental<br><br>Tel.: 0211 - 4056172<br>Mobil.: 0151-3389204<br>info@feldner-post.de</address>
  </aside>

  <footer class="abs footer">WWW.VORMA.DE HIER KOMMT DANN IHR FOOTER-BEREICH HIN, AUF WUNSCH</footer>
</div>
</body>
</html>
```